BrivoLane Ute.

I want the full logo on one side. And the other side the card if right Ralf the logo the left half orange like the car in the logo color with Danielle R Morrow
Founder and CEO
Email symbol then dmorrow@brivolaneute.com
Www symbol. Then Brivolaneute.com
Phone symbol then 413-926-BRIV
The very bottom would like Brivo Lane Ute is a division of Harmond Vistas. LLC

```html
<!DOCTYPE html>
<html lang="en">
<head>
<meta charset="utf-8">
<title>BrivoLane Ute – Business Card</title>
<link rel="stylesheet" href="https://fonts.googleapis.com/css2?family=Arimo:wght@400;700&display=swap">
<style>
  :root {
    --page-bg: #e9e6e1;
    --card-white: #f7f7f6;
    --amber-light: #f5c236;
    --amber-deep: #e5a01c;
    --ink: #1c1a17;
    --band: #111111;
    --paper-text: #ffffff;
    --divider: rgba(255,255,255,0.75);
  }
  * { box-sizing: border-box; margin: 0; padding: 0; }
  html, body {
    width: 1200px; height: 780px; overflow: hidden;
    background: var(--page-bg);
    font-family: "Arimo", Arial, sans-serif;
    color: var(--ink);
  }
  .canvas {
    width: 1200px; height: 780px;
    display: flex; flex-direction: column; align-items: center; justify-content: center;
    gap: 30px;
  }
  .card {
    width: 620px; height: 354px;
    position: relative;
    box-shadow: 0 6px 18px rgba(0,0,0,0.18);
    overflow: hidden;
  }

  /* Contact side */
  .card--contact { display: grid; grid-template-rows: 1fr 44px; }
  .card__halves { display: grid; grid-template-columns: 1fr 1fr; }
  .contact-panel {
    background: linear-gradient(160deg, var(--amber-light) 0%, var(--amber-deep) 100%);
    padding: 44px 24px 0 30px;
  }
  .contact-panel__name {
    font-weight: 700; font-size: 21px; letter-spacing: -0.2px;
    text-transform: uppercase; color: var(--ink);
  }
  .contact-panel__role {
    font-size: 16px; color: var(--paper-text); margin-top: 4px;
  }
  .contact-panel__rule {
    height: 1px; background: var(--divider); margin: 22px 0 18px 20px;
  }
  .contact-list { list-style: none; display: flex; flex-direction: column; gap: 11px; }
  .contact-list__item {
    display: flex; align-items: center; gap: 10px;
    font-size: 15px; color: var(--ink);
  }
  .contact-list__item:nth-child(2),
  .contact-list__item:nth-child(3) { color: var(--paper-text); }
  .contact-list__icon {
    width: 20px; height: 20px; border-radius: 50%;
    background: var(--ink);
    display: inline-flex; align-items: center; justify-content: center;
    flex: none;
  }
  .contact-list__icon svg { width: 12px; height: 12px; }

  .logo-panel {
    background: var(--card-white);
    display: flex; align-items: center; justify-content: center;
  }
  .division-band {
    background: var(--band);
    color: var(--paper-text);
    font-size: 15px; letter-spacing: 2.4px;
    display: flex; align-items: center; justify-content: center;
  }

  /* Logo lockup (name + single mark) */
  .brand {
    display: flex; align-items: center; gap: 12px;
  }
  .brand__dot {
    width: 22px; height: 22px; border-radius: 50%;
    background: var(--amber-deep); flex: none;
  }
  .brand__name {
    font-weight: 700; color: var(--ink); text-transform: uppercase;
    letter-spacing: 1px; white-space: nowrap;
  }
  .logo-panel .brand__name { font-size: 26px; }

  /* Logo side */
  .card--logo {
    background: linear-gradient(135deg, #ffffff 0%, #eeeeee 100%);
    display: flex; align-items: center; justify-content: center;
  }
  .card--logo .brand { gap: 18px; }
  .card--logo .brand__dot { width: 34px; height: 34px; }
  .card--logo .brand__name { font-size: 50px; }
</style>
</head>
<body>
<main class="canvas">

  <section class="card card--contact" aria-label="Business card, contact side">
    <div class="card__halves">
      <div class="contact-panel">
        <h1 class="contact-panel__name">Danielle R Morrow</h1>
        <p class="contact-panel__role">Founder and CEO</p>
        <div class="contact-panel__rule"></div>
        <ul class="contact-list">
          <li class="contact-list__item">
            <span class="contact-list__icon">
              <svg viewBox="0 0 24 24" fill="#f0b429"><path d="M6.6 10.8a15.1 15.1 0 0 0 6.6 6.6l2.2-2.2c.3-.3.7-.4 1-.2 1.1.4 2.3.6 3.6.6.6 0 1 .4 1 1V20c0 .6-.4 1-1 1A17 17 0 0 1 3 4c0-.6.4-1 1-1h3.5c.6 0 1 .4 1 1 0 1.3.2 2.5.6 3.6.1.3 0 .7-.2 1z"/></svg>
            </span>
            413-926-BRIV
          </li>
          <li class="contact-list__item">
            <span class="contact-list__icon">
              <svg viewBox="0 0 24 24" fill="none" stroke="#f0b429" stroke-width="2.4"><rect x="3" y="5" width="18" height="14" rx="1.5"/><path d="M3 6l9 7 9-7"/></svg>
            </span>
            dmorrow@brivolaneute.com
          </li>
          <li class="contact-list__item">
            <span class="contact-list__icon">
              <svg viewBox="0 0 24 24" fill="none" stroke="#f0b429" stroke-width="2.2"><circle cx="12" cy="12" r="9"/><path d="M3 12h18M12 3c3 3.2 3 14.8 0 18M12 3c-3 3.2-3 14.8 0 18"/></svg>
            </span>
            Brivolaneute.com
          </li>
        </ul>
        <div class="contact-panel__rule"></div>
      </div>
      <div class="logo-panel">
        <div class="brand">
          <span class="brand__dot"></span>
          <span class="brand__name">BrivoLane Ute</span>
        </div>
      </div>
    </div>
    <footer class="division-band">Brivo Lane Ute is a division of Harmond Vistas. LLC</footer>
  </section>

  <section class="card card--logo" aria-label="Business card, logo side">
    <div class="brand">
      <span class="brand__dot"></span>
      <span class="brand__name">BrivoLane Ute</span>
    </div>
  </section>

</main>
</body>
</html>
```